Brightwell Mechanical - Business Card Design

We would like a dark (likely black) themed business card to be able to hand out to potential clients. We may list our services on the card or keep it clean. Unsure. Logo attached

```html
<!DOCTYPE html>
<html lang="en">
<head>
<meta charset="UTF-8">
<title>Brightwell Mechanical – Business Card</title>
<link rel="stylesheet" href="https://fonts.googleapis.com/css2?family=Roboto:wght@400;500;700;900&display=swap">
<style>
  :root {
    --stage: #121212;
    --card: #1b1b1b;
    --mark-grey: #363636;
    --deco-grey: #222222;
    --accent-orange: #e8582a;
    --accent-blue: #2d7fc9;
    --text-muted: #9a9a9a;
    --icon-grey: #8a8a8a;
  }
  * { box-sizing: border-box; margin: 0; padding: 0; }
  html, body {
    width: 1200px; height: 1200px; overflow: hidden;
    background: var(--stage);
    font-family: "Roboto", Arial, sans-serif;
  }
  .stage {
    width: 1200px; height: 1200px;
    display: flex; flex-direction: column;
    align-items: center; justify-content: center;
    gap: 70px;
  }
  .card {
    position: relative;
    width: 640px; height: 380px;
    background: var(--card);
    border-radius: 0 30px 0 30px;
    overflow: hidden;
    box-shadow: 0 14px 40px rgba(0,0,0,0.55);
  }

  /* Front */
  .card--front {
    display: flex; flex-direction: column;
    align-items: center; justify-content: center;
    gap: 22px;
  }
  .brand-dot {
    width: 96px; height: 96px; border-radius: 50%;
    background: var(--mark-grey);
  }
  .brand-name {
    font-weight: 900;
    font-size: 46px;
    letter-spacing: 1px;
    text-transform: uppercase;
    color: var(--mark-grey);
    text-align: center;
    line-height: 1.05;
  }

  /* Back */
  .deco-circle {
    position: absolute;
    left: -10px; top: 80px;
    width: 250px; height: 250px;
    border-radius: 50%;
    background: var(--deco-grey);
  }
  .person {
    position: absolute; right: 42px; top: 50px;
    text-align: right;
  }
  .person__name {
    font-weight: 500; font-size: 34px; line-height: 1.1;
  }
  .person__first { color: var(--accent-orange); }
  .person__last { color: var(--accent-blue); }
  .person__title {
    margin-top: 14px;
    font-size: 16px; color: var(--text-muted);
    word-spacing: 3px;
  }
  .divider {
    position: absolute; left: 252px; right: 40px; top: 260px;
    height: 3px; background: var(--accent-orange);
  }
  .contacts {
    position: absolute; right: 40px; top: 272px;
    list-style: none;
  }
  .contacts li {
    display: flex; justify-content: flex-end; align-items: center;
    gap: 14px;
    font-size: 18px; line-height: 28px;
    color: var(--text-muted);
  }
  .contacts svg { width: 16px; height: 16px; flex: none; }
</style>
</head>
<body>
<main class="stage">
  <section class="card card--front">
    <div class="brand-dot"></div>
    <div class="brand-name">Brightwell<br>Mechanical Inc</div>
  </section>

  <section class="card card--back">
    <div class="deco-circle"></div>
    <div class="person">
      <h1 class="person__name"><span class="person__first">Daniel R.</span> <span class="person__last">Ashford</span></h1>
      <p class="person__title">RPhS, RVS, Founder</p>
    </div>
    <div class="divider"></div>
    <ul class="contacts">
      <li>(555) 014-2290
        <svg viewBox="0 0 16 16" aria-hidden="true"><rect x="4" y="1" width="8" height="14" rx="1.5" fill="none" stroke="var(--icon-grey)" stroke-width="1.6"/><rect x="6" y="3.5" width="4" height="5" fill="var(--icon-grey)"/></svg>
      </li>
      <li>Daniel@ClearwaterVascular.com
        <svg viewBox="0 0 16 16" aria-hidden="true"><rect x="1.5" y="3.5" width="13" height="9" fill="none" stroke="var(--icon-grey)" stroke-width="1.5"/><path d="M1.5 3.5 8 9l6.5-5.5" fill="none" stroke="var(--icon-grey)" stroke-width="1.5"/></svg>
      </li>
      <li>www.ClearwaterVascular.com
        <svg viewBox="0 0 16 16" aria-hidden="true"><circle cx="8" cy="8" r="6.5" fill="none" stroke="var(--icon-grey)" stroke-width="1.5"/><ellipse cx="8" cy="8" rx="2.8" ry="6.5" fill="none" stroke="var(--icon-grey)" stroke-width="1.2"/><path d="M1.5 8h13" stroke="var(--icon-grey)" stroke-width="1.2"/></svg>
      </li>
    </ul>
  </section>
</main>
</body>
</html>
```